TRENDY & MODERN BUSINESS CARD DESIGN for Media Company *

I need a minimalistic - clean - modern and professional business card layout and design for MEDIA & PHOTOGRAPHY STUDIO.

We do NOT have a logo, and not really looking for one - but rather excellent typography and design. We would consider the 3 as a focal point.

We do personal and commercial photography.

Target Market(s)

Personal and commercial photography clientele

Contact Information for Business Card

KYT size - from kyt.com / size guidelines are enclosed in the brief

Font styles to use
Sans Serif

Colors
f78f20
eda3c7
cee9f5
0555a3
e667a6
fbf289

Requirements
Must have
• Clean lines - Modern layout
Nice to have
• All blue background as an option - use color palette in brief please.
Should not have
• Old fashion fonts and regular fonts.

```html
<!DOCTYPE html>
<html lang="en">
<head>
<meta charset="UTF-8">
<title>Lumen Frame Studio – Business Card</title>
<link rel="stylesheet" href="https://fonts.googleapis.com/css2?family=Lato:wght@400&family=Rubik:wght@500;700&family=Oswald:wght@600&family=Barlow:wght@400&display=swap">
<style>
  :root {
    --page-bg: #e9e7e8;
    --front-pink: #ee5f98;
    --back-pink: #f497c0;
    --ink: #2a2a2c;
    --white: #ffffff;
  }
  * { margin: 0; padding: 0; box-sizing: border-box; }
  html, body { width: 1200px; height: 1200px; overflow: hidden; }
  body {
    background: var(--page-bg);
    display: flex;
    flex-direction: column;
    align-items: center;
    justify-content: center;
    gap: 60px;
  }
  .card {
    position: relative;
    width: 840px;
    height: 480px;
    box-shadow: 0 6px 18px rgba(0,0,0,0.12);
  }

  /* Front */
  .card--front {
    background: var(--front-pink);
    color: var(--white);
    font-family: 'Lato', sans-serif;
    text-align: center;
  }
  .front-brand {
    position: absolute;
    top: 170px;
    left: 0; right: 0;
  }
  .front-brand__name {
    font-weight: 400;
    font-size: 54px;
    letter-spacing: 2px;
    line-height: 1;
  }
  .front-brand__tagline {
    margin-top: 10px;
    font-weight: 400;
    font-size: 17px;
    letter-spacing: 5px;
  }
  .front-cities {
    position: absolute;
    bottom: 48px;
    left: 0; right: 0;
    font-size: 14px;
    letter-spacing: 4px;
  }

  /* Back */
  .card--back {
    background: var(--back-pink);
    color: var(--ink);
  }
  .back-brand {
    position: absolute;
    top: 52px;
    right: 56px;
    text-align: right;
    font-family: 'Rubik', sans-serif;
  }
  .back-brand__name {
    font-weight: 700;
    font-size: 50px;
    line-height: 1;
    letter-spacing: 1px;
  }
  .back-brand__tagline {
    margin-top: 4px;
    font-weight: 500;
    font-size: 17px;
    letter-spacing: 3.5px;
  }
  .contact {
    position: absolute;
    left: 56px;
    bottom: 50px;
  }
  .contact__head {
    display: flex;
    align-items: baseline;
    gap: 14px;
  }
  .contact__name {
    font-family: 'Oswald', sans-serif;
    font-weight: 600;
    font-size: 46px;
    line-height: 1;
    text-transform: uppercase;
  }
  .contact__role {
    font-family: 'Barlow', sans-serif;
    font-size: 19px;
  }
  .contact__details {
    margin-top: 10px;
    font-family: 'Barlow', sans-serif;
    font-size: 17px;
    word-spacing: 1px;
  }
  .contact__sep { margin: 0 10px; }
</style>
</head>
<body>

  <section class="card card--front">
    <div class="front-brand">
      <h1 class="front-brand__name">LUMEN FRAME STUDIO</h1>
      <p class="front-brand__tagline">HONEST IMAGES, LASTING STORIES</p>
    </div>
    <p class="front-cities">MIAMI · NEW YORK · LAS VEGAS · CANCUN · ROMA</p>
  </section>

  <section class="card card--back">
    <div class="back-brand">
      <h2 class="back-brand__name">LUMEN FRAME STUDIO</h2>
      <p class="back-brand__tagline">HONEST IMAGES - LASTING STORIES</p>
    </div>
    <div class="contact">
      <div class="contact__head">
        <span class="contact__name">Marisol Vega</span>
        <span class="contact__role">Founder &amp; Media Director</span>
      </div>
      <p class="contact__details">
        +(305) 555-0142<span class="contact__sep">/</span>mv@lumenframe.studio<span class="contact__sep">/</span>240 Harbor Lane, 9th Floor, Miami, FL 33130
      </p>
    </div>
  </section>

</body>
</html>
```